Business Card and Simple Logo Desgin

New Zealand based start up company "Brava Advisory LTD" requires business cards and simple logo design.

Card Content.

Brava Advisory LTD

Rosalind Kettering
CA, BMS (Hons)

r.kettering@bravaadvisory.example.nz
PH +64 21 705 146

Target Market(s)

Corporate Business in IT, Finance and accounting.

Industry/Entity Type

Business

```html
<!DOCTYPE html>
<html lang="en">
<head>
<meta charset="utf-8">
<title>Brava Advisory LTD — Business Card</title>
<link rel="stylesheet" href="https://fonts.googleapis.com/css2?family=Questrial&family=Quicksand:wght@300;400&display=swap">
<style>
  :root {
    --page: #e9e4dc;
    --card-top: #1d201f;
    --card-bottom: #433d3c;
    --panel-dark: #1c1f1e;
    --curve-light: #5a5352;
    --accent: #e3100f;
    --logo-text: #e2e2e2;
    --detail-text: #cfcfcf;
    --rule: #e6e6e6;
  }
  * { box-sizing: border-box; margin: 0; padding: 0; }
  html, body {
    width: 1200px;
    height: 900px;
    overflow: hidden;
    background: var(--page);
  }
  .sheet {
    position: relative;
    width: 1200px;
    height: 900px;
  }
  .card {
    position: absolute;
    left: 289px;
    width: 598px;
    height: 362px;
    overflow: hidden;
    background: linear-gradient(to bottom, var(--card-top) 0%, var(--card-top) 40%, var(--card-bottom) 100%);
    box-shadow: 0 6px 14px rgba(0, 0, 0, 0.25);
  }
  .card--front { top: 64px; }
  .card--back { top: 448px; }

  .brand {
    display: flex;
    align-items: center;
    gap: 8px;
    font-family: "Questrial", "Century Gothic", sans-serif;
    color: var(--logo-text);
    white-space: nowrap;
  }
  .brand__mark {
    display: block;
    background: var(--accent);
  }
  .card--front .brand {
    position: absolute;
    top: 160px;
    left: 0;
    right: 0;
    justify-content: center;
    font-size: 27px;
  }
  .card--front .brand__mark { width: 14px; height: 14px; }

  .back-art {
    position: absolute;
    inset: 0;
    width: 100%;
    height: 100%;
  }
  .card--back .brand {
    position: absolute;
    top: 16px;
    left: 14px;
    font-size: 18px;
    gap: 6px;
  }
  .card--back .brand__mark { width: 9px; height: 9px; }

  .contact {
    position: absolute;
    right: 32px;
    top: 240px;
    font-family: "Quicksand", "Poiret One", sans-serif;
    font-weight: 300;
    color: var(--detail-text);
    text-align: right;
  }
  .contact__group {
    display: flex;
    align-items: stretch;
    gap: 12px;
    justify-content: flex-end;
  }
  .contact__group + .contact__group { margin-top: 12px; }
  .contact__lines { display: flex; flex-direction: column; }
  .contact__rule {
    width: 3px;
    background: var(--rule);
    margin: 2px 0;
  }
  .contact__name, .contact__title { font-size: 15.5px; line-height: 23px; }
  .contact__email, .contact__phone { font-size: 13.5px; line-height: 18px; }
</style>
</head>
<body>
<main class="sheet">
  <section class="card card--front" aria-label="Card front">
    <div class="brand">
      <span class="brand__mark" aria-hidden="true"></span>
      <span class="brand__name">Brava Advisory LTD</span>
    </div>
  </section>

  <section class="card card--back" aria-label="Card back">
    <svg class="back-art" viewBox="0 0 598 362" preserveAspectRatio="none" aria-hidden="true">
      <defs>
        <linearGradient id="lowerFill" x1="0" y1="0" x2="0" y2="1">
          <stop offset="0" stop-color="#2a2a29"/>
          <stop offset="1" stop-color="#463f3e"/>
        </linearGradient>
      </defs>
      <rect width="598" height="362" fill="var(--panel-dark)"/>
      <path d="M0 245 C 70 95 240 22 590 6 L 598 6 L 598 362 L 0 362 Z" fill="url(#lowerFill)"/>
      <path d="M0 245 C 70 95 240 22 590 6" fill="none" stroke="var(--curve-light)" stroke-width="4"/>
    </svg>

    <div class="brand">
      <span class="brand__mark" aria-hidden="true"></span>
      <span class="brand__name">Brava Advisory LTD</span>
    </div>

    <div class="contact">
      <div class="contact__group">
        <div class="contact__lines">
          <span class="contact__name">Rosalind Kettering</span>
          <span class="contact__title">CA, BMS (Hons)</span>
        </div>
        <span class="contact__rule" aria-hidden="true"></span>
      </div>
      <div class="contact__group">
        <div class="contact__lines">
          <span class="contact__email">r.kettering@bravaadvisory.example.nz</span>
          <span class="contact__phone">PH +64 21 705 146</span>
        </div>
        <span class="contact__rule" aria-hidden="true"></span>
      </div>
    </div>
  </section>
</main>
</body>
</html>
```